Wine Bottle Label

Project: New Label for Marlow Wine

Sponsored by: Tall Oak Cellars (talloakcellars.example and Castellane Wines, producer of Marlow Wines)

Product Description:

Wine comes in both red (cabernet, zinfandel) and white (Chardonnay, Sauvignon Blanc). It is marketed to restaurants and mid priced retailers including Harbor Pantry, etc.) Wine is priced between $17 - $20 per bottle. The wine is in the medium price category and is intended for mid market appeal.

_
Label Requirements:

• Noticeable among other labels when on a black bottle. White labels are most noticeable but all color choices are an option if the brand stands out and can be easily recognizable from 10 – 12ft.

• Has to appeal to Gen X - younger people. Contemporary. Must appeal to women who buy the majority of wine in the US.

• Has to be presentable at the dinner table...slightly sophisticated.

• Has to connect with the “Official Bird of the Fenwick Nature League” Great White Marlow

• Bird is most often seen in grassy green pasture/meadows or wading in shallow water. Alone or in group.

• Has to fit on the bottle: Label size: 3 ½” H – 2 ¾” W

• Keep it Simple, lots of empty space

• Could be free form graphic design, illustrations, photos, etc.

• Could be abstract representation providing it connects to Egrets, e.g. stamp of foot which is gold embossed or similar.)

• Label must contain:

o Brand Name: Marlow
o Varietal: will vary (Cabernet Sauvignon, Chardonnay, Sauvignon Blanc, Zinfandel, etc.)
o Appellation: varies (Sonoma County, Napa Valley, California)
o Vintage: 2010, 2011, etc.

• Variations in label color/design are possible between varietals but brand should be consistent.

Back design must also be included. Example of current back with text is attached.

Requirements
Must have
• Must have relationship with Marlow Bird - figuratively or literally
Has to fit on the bottle: Label size: 3 ½” H – 2 ¾” W
o Brand Name: Marlow

```html
<!DOCTYPE html>
<html lang="en">
<head>
<meta charset="utf-8">
<title>Marlow Wine – Label Range</title>
<link rel="stylesheet" href="https://fonts.googleapis.com/css2?family=Great+Vibes&family=Oswald:wght@400&family=Playfair+Display:ital,wght@1,700&family=Arimo:wght@400&display=swap">
<style>
  :root {
    --backdrop-inner: #ffffff;
    --backdrop-outer: #dcdcdc;
    --label-green: #9dc435;
    --label-red: #c1171f;
    --label-orange: #f7a61f;
    --label-blue: #0b4ea2;
    --label-ink: #ffffff;
    --band-black: #111111;
    --motif-pink: #e2337a;
    --motif-gold: #f0b93a;
    --motif-violet: #8a4fb8;
  }
  * { box-sizing: border-box; margin: 0; padding: 0; }
  html, body { width: 1200px; height: 1000px; overflow: hidden; }
  body {
    background: radial-gradient(ellipse at 50% 40%, var(--backdrop-inner) 0%, var(--backdrop-outer) 100%);
    position: relative;
  }
  .label-range {
    position: absolute;
    left: 88px;
    top: 450px;
    display: flex;
    gap: 53px;
  }
  .label {
    position: relative;
    width: 212px;
    height: 340px;
    color: var(--label-ink);
    overflow: hidden;
  }
  .label--sauvignon-blanc { background: var(--label-green); }
  .label--chardonnay { background: var(--label-red); }
  .label--cabernet { background: var(--label-orange); }
  .label--zinfandel { background: var(--label-blue); }

  .label__brand {
    position: absolute;
    top: 28px;
    left: 0;
    width: 100%;
    text-align: center;
    font-family: "Great Vibes", cursive;
    font-weight: 400;
    font-size: 54px;
    line-height: 1;
  }
  .label__motif {
    position: absolute;
    left: 0;
    top: 150px;
    width: 112px;
    height: 160px;
    background: linear-gradient(160deg, var(--motif-violet) 0%, var(--motif-gold) 30%, var(--motif-pink) 70%, var(--motif-pink) 100%);
    border-top-right-radius: 56px;
  }
  .label__details {
    position: absolute;
    left: 120px;
    right: 4px;
    top: 170px;
    white-space: nowrap;
  }
  .label__vintage {
    font-family: "Playfair Display", serif;
    font-style: italic;
    font-weight: 700;
    font-size: 13px;
    line-height: 1.1;
  }
  .label__varietal {
    font-family: "Oswald", sans-serif;
    font-weight: 400;
    font-size: 15px;
    line-height: 1.05;
    text-transform: uppercase;
  }
  .label__rule {
    border: none;
    border-top: 2px solid var(--label-ink);
    margin: 5px 0 5px;
  }
  .label__appellation {
    font-family: "Playfair Display", serif;
    font-style: italic;
    font-weight: 700;
    font-size: 11px;
  }
  .label__band {
    position: absolute;
    left: 0;
    bottom: 0;
    width: 100%;
    height: 30px;
    background: var(--band-black);
    display: flex;
    justify-content: space-between;
    align-items: center;
    padding: 0 12px 0 72px;
    font-family: "Arimo", sans-serif;
    font-size: 9px;
  }
</style>
</head>
<body>
  <main class="label-range">
    <article class="label label--sauvignon-blanc">
      <h1 class="label__brand">Marlow</h1>
      <div class="label__motif" role="img" aria-label="Colourful paisley flourish illustration"></div>
      <div class="label__details">
        <p class="label__vintage">2011</p>
        <p class="label__varietal">Sauvignon<br>Blanc</p>
        <hr class="label__rule">
        <p class="label__appellation">California</p>
      </div>
      <footer class="label__band"><span>ALC 13.5% BY VOL</span><span>750ML</span></footer>
    </article>

    <article class="label label--chardonnay">
      <h1 class="label__brand">Marlow</h1>
      <div class="label__motif" role="img" aria-label="Colourful paisley flourish illustration"></div>
      <div class="label__details">
        <p class="label__vintage">2011</p>
        <p class="label__varietal">Chardonnay</p>
        <hr class="label__rule">
        <p class="label__appellation">California</p>
      </div>
      <footer class="label__band"><span>ALC 13.5% BY VOL</span><span>750ML</span></footer>
    </article>

    <article class="label label--cabernet">
      <h1 class="label__brand">Marlow</h1>
      <div class="label__motif" role="img" aria-label="Colourful paisley flourish illustration"></div>
      <div class="label__details">
        <p class="label__vintage">2010</p>
        <p class="label__varietal">Cabernet<br>Sauvignon</p>
        <hr class="label__rule">
        <p class="label__appellation">California</p>
      </div>
      <footer class="label__band"><span>ALC 13.5% BY VOL</span><span>750ML</span></footer>
    </article>

    <article class="label label--zinfandel">
      <h1 class="label__brand">Marlow</h1>
      <div class="label__motif" role="img" aria-label="Colourful paisley flourish illustration"></div>
      <div class="label__details">
        <p class="label__vintage">2011</p>
        <p class="label__varietal">Zinfandel</p>
        <hr class="label__rule">
        <p class="label__appellation">California</p>
      </div>
      <footer class="label__band"><span>ALC 13.5% BY VOL</span><span>750ML</span></footer>
    </article>
  </main>
</body>
</html>
```